Need a business card for our overland brand!

We had the logo made and we need a great design for our business card. Use the logo provide or tweak it however you see fit.

Contact Information for Business Card

Name, Title, Telephone, email, website

```html
<!DOCTYPE html>
<html lang="en">
<head>
<meta charset="utf-8">
<title>Ridgeline Expeditions – Business Card</title>
<link rel="stylesheet" href="https://fonts.googleapis.com/css2?family=Montserrat:wght@400;500;700;800&display=swap">
<style>
  :root {
    --navy: #243a53;
    --sky: #1f9fc4;
    --paper: #ffffff;
    --backdrop: #d9d8d5;
    --ink: #1e1e1e;
  }
  * { box-sizing: border-box; margin: 0; padding: 0; }
  html, body { width: 1200px; height: 801px; overflow: hidden; }
  body {
    background: var(--backdrop);
    font-family: "Montserrat", sans-serif;
    position: relative;
  }
  .card {
    position: absolute;
    top: 246px;
    width: 540px;
    height: 309px;
    background: var(--paper);
    border-radius: 18px;
    overflow: hidden;
    box-shadow: 0 10px 26px rgba(0,0,0,.18);
  }
  .card--front { left: 40px; border-bottom: 3px solid var(--sky); }
  .card--back { left: 620px; border-bottom: 3px solid var(--sky); }
  .card__shapes { position: absolute; inset: 0; }
  .brand {
    position: absolute;
    color: var(--navy);
    font-weight: 800;
    text-transform: uppercase;
    line-height: 1.02;
    letter-spacing: .3px;
  }
  .card--front .brand { left: 66px; top: 128px; font-size: 21px; }
  .card--back .brand { left: 0; right: 0; top: 100px; text-align: center; font-size: 50px; }
  .divider {
    position: absolute;
    left: 262px; top: 62px;
    width: 1.5px; height: 186px;
    background: var(--sky);
  }
  .contact { position: absolute; left: 282px; top: 58px; color: var(--ink); }
  .contact__name { color: var(--sky); font-weight: 700; font-size: 19px; letter-spacing: 1px; }
  .contact__title { font-size: 12.5px; margin-top: 2px; }
  .contact__list { list-style: none; margin-top: 14px; font-size: 12px; line-height: 19px; }
  .contact__list li { display: flex; align-items: center; gap: 7px; }
  .icon { width: 12px; height: 12px; flex: none; }
  .contact__address { font-size: 12px; line-height: 17px; margin-top: 12px; }
</style>
</head>
<body>
  <section class="card card--front">
    <svg class="card__shapes" viewBox="0 0 540 309" aria-hidden="true">
      <path d="M0,100 A300,300 0 0,0 64,309 L0,309 Z" fill="var(--sky)"/>
      <path d="M20,88 A300,300 0 0,0 82,309" fill="none" stroke="var(--sky)" stroke-width="2.5"/>
      <path d="M540,200 A300,300 0 0,0 478,0 L540,0 Z" fill="var(--navy)"/>
      <path d="M520,212 A300,300 0 0,0 460,0" fill="none" stroke="var(--sky)" stroke-width="2.5"/>
    </svg>
    <div class="brand">Ridgeline<br>Expeditions</div>
    <div class="divider"></div>
    <div class="contact">
      <h1 class="contact__name">DANIEL HART</h1>
      <p class="contact__title">Managing Director</p>
      <ul class="contact__list">
        <li><svg class="icon" viewBox="0 0 12 12"><path d="M2 1h3l1 3-1.5 1a6 6 0 0 0 2.5 2.5L8 6l3 1v3a1 1 0 0 1-1 1A9 9 0 0 1 1 2a1 1 0 0 1 1-1z" fill="var(--sky)"/></svg>555 014 2368</li>
        <li><svg class="icon" viewBox="0 0 12 12"><rect x="0.5" y="2" width="11" height="8" rx="1" fill="var(--sky)"/><path d="M1 3l5 4 5-4" fill="none" stroke="#fff" stroke-width="1"/></svg>info@ridgelinemail.com</li>
        <li><svg class="icon" viewBox="0 0 12 12"><circle cx="6" cy="6" r="5.5" fill="var(--sky)"/><path d="M0.5 6h11M6 .5c-3 3-3 8 0 11M6 .5c3 3 3 8 0 11" fill="none" stroke="#fff" stroke-width=".8"/></svg>www.ridgelineexp.com</li>
      </ul>
      <p class="contact__address">Your address, City<br>State, Zip 1234</p>
    </div>
  </section>

  <section class="card card--back">
    <div class="brand">Ridgeline<br>Expeditions</div>
  </section>
</body>
</html>
```